A brand new wordpress website for my business which will replace my current site www.harbornetcall.com.au, As i rank quite well in google will it be ok to keep my current URL's. I sell the following service and products

1. Voip Provider (Main service) we sell directly the the end user but also we would like to get resellers and agents to sell our services. agents selling our brand resellers sell our services branded as theirs
2. Hosted Pbx (main service) home page must push this service explaining the benifits and features that come with a hosted pbx, we also have business plans based on number of extensions (phones) the customer requires
3. Tornax IP Pbx (product) only selling IP Pbx and selected software
4. Velbox IP Pbx (product)
5. Quorvin IP Phones (this is the main VoIP phone we sell)
6. lumora phones (to be on a landing page only not apart of the main site)
7. selected headsets from Dravensonic (products)
8. Meridal Conference phone (VoIP model only)
9. we can supply fax to email service

we would like a support page with user guides (step by step instructions on our products and services and FAQ's about all products and services

we have a carrier grade softswitch (telco billing system) z7ledger http://www.pinwheelledger.org this system has a ticketing system, customer and agent login I would like a URL link from our website so customers can login to this system. also it is possible to skin z7ledger to look like our website

VoIP business plans

$0 per month
call rate .12c land line calls
.24c per minute mobile calls

$25 per month
250 Free local land line calls
call rate is .10c land line calls .22c per minute mobile calls

$50 per month
500 Free local land line calls
call rate .09 land line calls .20c per minute mobile calls

$100 per month
1000 free local land line calls
call rate .08c land line calls .18c per minute mobile calls

all mobile calls are billed per second no flag fall

also require a link to international call rates

We can port your existing telephone number from any carrier or supply new Australian telephone numbers

02, 03, 07, 08, 131, 1300, 1800

Designs i like www.tralcom.com.au and www.orbitelphone.com

I would like the website to be white and bright

Reason: Please use images of the products I sell only

Target Market(s)

business customers only

Industry/Entity Type

Requirements
Must have
• all pages must have its own banner to reflect the product or service we are selling. the home page can automatically change to show all pages with a link straight to the page in question

for example if on the home page the banner for quorvin phone is displaying if someone click on the banner they will be redirected to the quorvin page

Must Be SEO friendly
Nice to have
• shopping cart via paypal for all products but before customer checks out i would like to offer two options

1. Pre configure the item and ship to your address for existing customers
2. would you like a harbor net call technician to attend your office and install the item in person (costs involved $60 call out fee $120 per hours every item sold charge .50 hour and only the one call out fee)

new and existing customers can book service work via the website
1. describe the work required (maybe we need to give a few option)
2. company details
3. pre payment (checkout via paypal) can we put the paypal fees back on to the customer?

```html
<!DOCTYPE html>
<html lang="en">
<head>
<meta charset="utf-8">
<title>harbor net call — Hosted PBX &amp; VoIP for Business</title>
<link rel="stylesheet" href="https://fonts.googleapis.com/css2?family=Open+Sans:wght@400;600;700;800&family=Oswald:wght@400;500;600&display=swap">
<style>
:root{
  --blue:#1c64b4;
  --blue-dark:#0d3d75;
  --blue-deep:#0a2f5c;
  --blue-light:#2f86d8;
  --sky:#e9f2fb;
  --ink:#2b2f36;
  --muted:#6b7380;
  --line:#dde3ea;
  --grey:#f3f5f8;
  --white:#ffffff;
  --green:#3ca83c;
  --orange:#f29a1f;
}
*{box-sizing:border-box;margin:0;padding:0}
html,body{width:1200px;height:2288px;overflow:hidden}
body{font-family:"Open Sans",Arial,sans-serif;color:var(--ink);background:var(--white);font-size:12px;line-height:1.5}
.wrap{width:960px;margin:0 auto;position:relative}
a{color:inherit;text-decoration:none}

/* header */
.site-header{height:88px}
.site-header .wrap{display:flex;align-items:center;justify-content:space-between;height:88px}
.brand{display:flex;align-items:center;gap:10px;font-weight:700;font-size:24px;color:var(--blue);letter-spacing:.3px}
.brand-mark{width:22px;height:22px;border-radius:50%;background:var(--blue)}
.call-box{display:flex;align-items:center;gap:10px;color:var(--muted);font-size:11px}
.call-box strong{font-family:"Oswald",sans-serif;font-size:30px;color:var(--blue);font-weight:500;letter-spacing:.5px}
.main-nav{height:32px;background:var(--blue)}
.main-nav ul{list-style:none;display:flex;height:32px;align-items:center}
.main-nav li{color:var(--white);font-size:11px;font-weight:600;padding:0 18px;border-right:1px solid rgba(255,255,255,.18);line-height:32px}
.main-nav li.active{background:var(--blue-dark)}

/* hero */
.hero{height:400px;background:linear-gradient(180deg,#0f4a8e 0%,#1b6cc2 60%,#0e4a8c 100%);position:relative;overflow:hidden}
.hero .wrap{height:400px}
.hero-copy{position:absolute;left:0;top:44px;width:430px;color:var(--white)}
.hero-title{font-family:"Oswald",sans-serif;font-size:48px;font-weight:500;line-height:1}
.hero-title span{font-size:30px;font-weight:400;margin-left:6px}
.hero-lead{font-size:11px;opacity:.85;margin:12px 0 16px;width:400px}
.feature-box{background:rgba(6,30,66,.55);border:1px solid rgba(255,255,255,.2);padding:12px 16px;width:370px}
.feature-box h3{font-size:15px;font-weight:700;margin-bottom:6px}
.feature-box li{list-style:none;display:flex;gap:8px;align-items:center;font-size:12px;font-weight:600;padding:3px 0}
.btn{display:inline-block;font-weight:700;font-size:11px;text-transform:uppercase;letter-spacing:.4px;padding:9px 18px;border-radius:2px}
.btn-light{background:var(--white);color:var(--blue-dark);margin-top:16px}
.hero-phone{position:absolute;right:60px;top:36px;width:430px;height:320px;border-radius:6px;background:linear-gradient(160deg,#3a3f47 0%,#16191d 70%,#2a2e34 100%)}
.chat-tab{position:absolute;right:0;top:500px;width:24px;height:90px;background:var(--blue);color:var(--white);font-size:10px;font-weight:700;writing-mode:vertical-rl;text-align:center;line-height:24px;border-radius:3px 0 0 3px;z-index:3}

/* intro */
.intro{height:260px;padding-top:32px}
.intro .wrap{display:flex;gap:40px}
.intro-text{flex:1}
.section-title{font-family:"Oswald",sans-serif;font-size:24px;font-weight:500;color:var(--blue)}
.intro-text p{color:var(--muted);font-size:11px;margin:8px 0 16px}
.btn-blue{background:var(--blue);color:var(--white)}
.benefits{width:330px;border:1px solid var(--line);background:var(--grey);padding:12px 16px}
.benefits h3{font-size:14px;font-weight:600;color:var(--ink);border-bottom:1px solid var(--line);padding-bottom:6px;margin-bottom:6px}
.benefits li{list-style:none;display:flex;gap:8px;align-items:center;font-size:11px;color:var(--muted);padding:3px 0}

/* products / services */
.catalog{text-align:center}
.catalog.products{height:270px;padding-top:8px}
.catalog.services{height:270px;padding-top:8px}
.catalog h2{font-family:"Oswald",sans-serif;font-size:22px;font-weight:500;color:var(--blue)}
.catalog .sub{font-size:13px;color:var(--ink);margin-bottom:16px}
.cards{display:flex;justify-content:space-between}
.card{width:176px;border:1px solid var(--line);background:var(--white)}
.card-img{height:82px;background:linear-gradient(180deg,#f7f8fa,#d9dde3)}
.card-img.dark{background:linear-gradient(180deg,#e9edf2,#7d8794)}
.card-label{background:var(--grey);border-top:1px solid var(--line);border-bottom:1px solid var(--line);font-size:10px;font-weight:700;padding:5px 0;color:var(--ink)}
.card p{font-size:10px;color:var(--muted);padding:8px 10px 6px;line-height:1.4}
.btn-more{background:var(--blue-dark);color:var(--white);font-size:9px;font-weight:700;padding:4px 14px;display:inline-block;margin-bottom:10px}

/* plans */
.plans{height:240px;text-align:center;padding-top:4px}
.plans h2{font-family:"Oswald",sans-serif;font-size:22px;font-weight:500;color:var(--blue);margin-bottom:10px}
.plan-table{margin:0 auto;border-collapse:collapse;width:760px;font-size:10px}
.plan-table th{background:var(--blue-dark);color:var(--white);font-weight:700;padding:6px;width:140px}
.plan-table th.row-head{background:transparent;width:200px}
.plan-table td{border:1px solid var(--line);padding:6px;color:var(--muted)}
.plan-table td.row-head{text-align:left;font-weight:600;color:var(--ink);background:var(--grey)}
.plan-table .price td{background:var(--blue);color:var(--white)}
.plan-table .price td.row-head{background:transparent;border:none}
.price strong{font-family:"Oswald",sans-serif;font-size:22px;font-weight:500;margin-right:4px}
.plan-table .featured{background:var(--blue-light) !important;color:var(--white)}
.plan-table th.featured{background:var(--blue-deep) !important;font-size:12px;padding:10px 6px}
.plan-table .blank{border:none;background:none;padding:6px 0 0}
.btn-signup{background:var(--orange);color:var(--white);font-size:9px;font-weight:700;padding:5px 12px;display:inline-block;line-height:1.4}

/* nbn band */
.nbn{height:80px;display:flex;align-items:center}
.nbn .wrap{border:1px solid var(--line);background:var(--sky);display:flex;align-items:center;justify-content:space-between;padding:12px 24px}
.nbn h3{font-size:16px;font-weight:800;color:var(--blue)}
.nbn p{font-size:10px;color:var(--muted)}
.btn-call{background:var(--blue);color:var(--white);font-size:13px;padding:10px 30px}

/* testimonial */
.testimonial{height:290px;padding-top:20px}
.testimonial .wrap{display:flex;justify-content:space-between}
.quote-block{width:560px}
.quote-block h2{font-size:30px;font-weight:800;line-height:1.1;color:var(--blue-light);letter-spacing:-.3px}
.quote-block h2 span{color:var(--blue-dark)}
.quote-row{display:flex;gap:16px;margin-top:22px;align-items:flex-start}
.avatar{width:70px;height:70px;border-radius:50%;background:#c5ccd6;flex-shrink:0}
.quote-row blockquote{font-size:12px;color:var(--muted);font-style:italic}
.quote-row cite{display:block;font-style:normal;font-weight:700;color:var(--ink);margin-top:8px;font-size:11px}
.promo{width:280px;height:250px;background:linear-gradient(160deg,#1e2530,#06090d);color:var(--white);padding:18px;position:relative;overflow:hidden}
.promo h3{font-family:"Oswald",sans-serif;font-size:26px;font-weight:500;line-height:1.05;color:var(--orange);white-space:nowrap}
.promo h3 span{display:block;color:var(--white);font-size:19px;margin-top:2px}
.promo p{font-size:10px;opacity:.8;margin-top:10px;width:100px;line-height:1.45}
.promo-img{position:absolute;right:16px;bottom:16px;width:136px;height:140px;background:linear-gradient(160deg,#4a515c,#1a1d22);border-radius:4px}

/* footer */
.site-footer{height:322px;background:var(--blue);color:var(--white);padding-top:36px}
.site-footer .wrap{display:flex;justify-content:space-between}
.foot-col{width:210px}
.foot-col h4{font-size:12px;font-weight:700;letter-spacing:.5px;margin-bottom:12px;text-transform:uppercase}
.foot-col li{list-style:none;font-size:11px;padding:4px 0;border-bottom:1px solid rgba(255,255,255,.12);opacity:.9}
.social li{display:flex;gap:10px;align-items:center;border:none;padding:5px 0}
.social i{width:18px;height:18px;background:rgba(255,255,255,.85);display:inline-block}
.contact p{font-size:11px;opacity:.9;margin-bottom:8px}
.bottom-bar{height:36px;background:var(--blue-deep);color:rgba(255,255,255,.75);font-size:10px;text-align:center;line-height:36px}
</style>
</head>
<body>

<header class="site-header">
  <div class="wrap">
    <a class="brand" href="#"><span class="brand-mark"></span>harbor net call</a>
    <div class="call-box">
      <svg width="22" height="22" viewBox="0 0 24 24"><path fill="#1c64b4" d="M6.6 10.8a15.1 15.1 0 0 0 6.6 6.6l2.2-2.2c.3-.3.7-.4 1-.2 1.1.4 2.3.6 3.6.6.6 0 1 .4 1 1V20c0 .6-.4 1-1 1A17 17 0 0 1 3 4c0-.6.4-1 1-1h3.5c.6 0 1 .4 1 1 0 1.3.2 2.5.6 3.6.1.3 0 .7-.2 1z"/></svg>
      <span>GIVE US A CALL<br>FOR HELP</span>
      <strong>1300 555 018</strong>
    </div>
  </div>
</header>

<nav class="main-nav">
  <div class="wrap">
    <ul>
      <li class="active">Home</li><li>Products</li><li>About Us</li><li>Hosted PBX</li><li>Contact Us</li><li>Telephone Systems</li><li>Plans &amp; Signup</li>
    </ul>
  </div>
</nav>

<section class="hero">
  <div class="wrap">
    <div class="hero-copy">
      <h1 class="hero-title">Hosted PBX<span>VoIP phone</span></h1>
      <p class="hero-lead">Hosted PBX is a cloud based phone system designed for growing businesses. No hardware to maintain, no lock in contracts.</p>
      <div class="feature-box">
        <h3>Features &amp; Benefits</h3>
        <ul>
          <li><svg width="12" height="12" viewBox="0 0 12 12"><path d="M1 6l3 3 7-7" stroke="#fff" stroke-width="2" fill="none"/></svg>As Many Extensions as You Need</li>
          <li><svg width="12" height="12" viewBox="0 0 12 12"><path d="M1 6l3 3 7-7" stroke="#fff" stroke-width="2" fill="none"/></svg>Completely Customisable Auto Attendant</li>
          <li><svg width="12" height="12" viewBox="0 0 12 12"><path d="M1 6l3 3 7-7" stroke="#fff" stroke-width="2" fill="none"/></svg>Send Voicemail To Your Email as Wav File</li>
          <li><svg width="12" height="12" viewBox="0 0 12 12"><path d="M1 6l3 3 7-7" stroke="#fff" stroke-width="2" fill="none"/></svg>All Extensions are Conference</li>
        </ul>
      </div>
      <a class="btn btn-light" href="#">View More</a>
    </div>
    <div class="hero-phone" role="img" aria-label="Photo of a desk IP phone with handset and colour display"></div>
  </div>
</section>

<a class="chat-tab" href="#">LIVE CHAT</a>

<section class="intro">
  <div class="wrap">
    <div class="intro-text">
      <h2 class="section-title">Hosted Pbx</h2>
      <p>Hosted PBX is a fully featured phone system delivered over the internet. Your calls are routed through our carrier grade network, giving your business enterprise features at a fraction of the cost of a traditional system. Add or remove extensions as your team changes, keep your existing numbers, and manage call flows from any browser. Every plan includes voicemail to email, call recording, ring groups and auto attendant with local support from our Australian technicians.</p>
      <a class="btn btn-blue" href="#">Try our service for a full 30 days free</a>
    </div>
    <aside class="benefits">
      <h3>Features &amp; Benefits</h3>
      <ul>
        <li><svg width="10" height="10" viewBox="0 0 12 12"><path d="M1 6l3 3 7-7" stroke="#1c64b4" stroke-width="2" fill="none"/></svg>No lock in contracts and free setup</li>
        <li><svg width="10" height="10" viewBox="0 0 12 12"><path d="M1 6l3 3 7-7" stroke="#1c64b4" stroke-width="2" fill="none"/></svg>Keep your existing business numbers</li>
        <li><svg width="10" height="10" viewBox="0 0 12 12"><path d="M1 6l3 3 7-7" stroke="#1c64b4" stroke-width="2" fill="none"/></svg>Voicemail delivered straight to email</li>
        <li><svg width="10" height="10" viewBox="0 0 12 12"><path d="M1 6l3 3 7-7" stroke="#1c64b4" stroke-width="2" fill="none"/></svg>Auto attendant and ring groups</li>
        <li><svg width="10" height="10" viewBox="0 0 12 12"><path d="M1 6l3 3 7-7" stroke="#1c64b4" stroke-width="2" fill="none"/></svg>Works from office, home or mobile</li>
        <li><svg width="10" height="10" viewBox="0 0 12 12"><path d="M1 6l3 3 7-7" stroke="#1c64b4" stroke-width="2" fill="none"/></svg>Local support seven days a week</li>
      </ul>
    </aside>
  </div>
</section>

<section class="catalog products">
  <div class="wrap">
    <h2>VOIP Products</h2>
    <p class="sub">Small to Medium Business Phone Systems &amp; Hosted PBX Solutions</p>
    <div class="cards">
      <article class="card"><div class="card-img" role="img" aria-label="Quorvin IP desk phone"></div><div class="card-label">QUORVIN PHONES</div><p>Business grade IP phones with HD voice, ready to plug in.</p><a class="btn-more" href="#">MORE</a></article>
      <article class="card"><div class="card-img" role="img" aria-label="Tornax IP PBX unit"></div><div class="card-label">TORNAX PBX</div><p>On premise IP PBX hardware with selected software options.</p><a class="btn-more" href="#">MORE</a></article>
      <article class="card"><div class="card-img" role="img" aria-label="Fax machine for fax to email"></div><div class="card-label">FAX TO EMAIL</div><p>Receive faxes as PDF files straight into your inbox.</p><a class="btn-more" href="#">MORE</a></article>
      <article class="card"><div class="card-img" role="img" aria-label="Dravensonic office headset"></div><div class="card-label">HEADSETS</div><p>Selected Dravensonic headsets for busy office teams.</p><a class="btn-more" href="#">MORE</a></article>
      <article class="card"><div class="card-img dark" role="img" aria-label="Meridal VoIP conference phone"></div><div class="card-label">CONFERENCE PHONE</div><p>Meridal VoIP conference phones for clear meeting calls.</p><a class="btn-more" href="#">MORE</a></article>
    </div>
  </div>
</section>

<section class="catalog services">
  <div class="wrap">
    <h2>VoIP Services</h2>
    <p class="sub">Small to Medium Business Phone Systems &amp; Hosted PBX Solutions</p>
    <div class="cards">
      <article class="card"><div class="card-img" role="img" aria-label="Hosted PBX desk phone"></div><div class="card-label">HOSTED PBX</div><p>Cloud phone system with every feature your office needs.</p><a class="btn-more" href="#">MORE</a></article>
      <article class="card"><div class="card-img" role="img" aria-label="VoIP provider phone handset"></div><div class="card-label">VOIP PROVIDER</div><p>Low call rates on a carrier grade Australian network.</p><a class="btn-more" href="#">MORE</a></article>
      <article class="card"><div class="card-img" role="img" aria-label="Technician servicing office equipment"></div><div class="card-label">ONSITE MAINTENANCE</div><p>Book a technician to install and service at your office.</p><a class="btn-more" href="#">MORE</a></article>
      <article class="card"><div class="card-img" role="img" aria-label="Office phone system audit"></div><div class="card-label">OFFICE AUDIT</div><p>We review your current setup and show where to save.</p><a class="btn-more" href="#">MORE</a></article>
      <article class="card"><div class="card-img" role="img" aria-label="Number porting desk phone"></div><div class="card-label">NUMBER PORTING</div><p>Keep your numbers or choose new 02, 03, 07, 08, 1300, 1800.</p><a class="btn-more" href="#">MORE</a></article>
    </div>
  </div>
</section>

<section class="plans">
  <div class="wrap">
    <h2>VoIP Business Plans</h2>
    <table class="plan-table">
      <tr><th class="row-head"></th><th>BUSINESS STARTER</th><th>BUSINESS SAVER</th><th class="featured">SUPER SAVER</th><th>EXTREME SAVER</th></tr>
      <tr class="price"><td class="row-head"></td><td><strong>$0</strong>per month</td><td><strong>$25</strong>per month<br>250 free local calls</td><td class="featured"><strong>$50</strong>per month<br>500 free local calls</td><td><strong>$100</strong>per month<br>1000 free local calls</td></tr>
      <tr><td class="row-head">Land line call</td><td>12c per call</td><td>10c per call</td><td>9c per call</td><td>8c per call</td></tr>
      <tr><td class="row-head">Mobile call</td><td>24c per minute</td><td>22c per minute</td><td>20c per minute</td><td>18c per minute</td></tr>
      <tr><td class="blank"></td><td class="blank"></td><td class="blank"></td><td class="blank"><a class="btn-signup" href="#">SIGNUP NOW</a></td><td class="blank"></td></tr>
    </table>
  </div>
</section>

<section class="nbn">
  <div class="wrap">
    <div>
      <h3>SMALL BUSINESS PHONE SYSTEMS READY FOR THE NBN</h3>
      <p>Mobile calls billed per second with no flag fall — view international call rates</p>
    </div>
    <a class="btn btn-call" href="#">CALL US NOW</a>
  </div>
</section>

<section class="testimonial">
  <div class="wrap">
    <div class="quote-block">
      <h2>LOVED BY OVER 250,00 USERS<br><span>AROUND THE WORLD.</span></h2>
      <div class="quote-row">
        <div class="avatar" role="img" aria-label="Customer portrait"></div>
        <blockquote>“Switching our office to hosted PBX cut our phone bill in half and the setup was done in a single afternoon. Support has been quick every time.”<cite>Office Manager, Sydney</cite></blockquote>
      </div>
    </div>
    <aside class="promo">
      <h3>FREE 24 MONTH PLAN<span>with every phone</span></h3>
      <p>Sign up today and get a free plan on selected IP phones.</p>
      <div class="promo-img" role="img" aria-label="Quorvin IP phone product photo"></div>
    </aside>
  </div>
</section>

<footer class="site-footer">
  <div class="wrap">
    <div class="foot-col">
      <h4>Home</h4>
      <ul><li>About Us</li><li>Hosted PBX</li><li>Products</li><li>Contact Us</li><li>Telephone Systems</li><li>Plans &amp; Signup</li></ul>
    </div>
    <div class="foot-col">
      <h4>Other Links</h4>
      <ul><li>Support &amp; User Guides</li><li>FAQs</li><li>Customer Login</li><li>International Call Rates</li><li>Resellers &amp; Agents</li></ul>
    </div>
    <div class="foot-col social">
      <h4>We Are Social</h4>
      <ul><li><i></i>Friendline</li><li><i></i>Chirpnet</li><li><i></i>Circlespace</li><li><i></i>Linkpro</li></ul>
    </div>
    <div class="foot-col contact">
      <h4>Contact Us</h4>
      <p>Level 3, 88 Wharfside Rd, Sydney NSW 2000</p>
      <p>Phone: 1300 555 018</p>
      <p>Email: hello@harbornetcall.com.au</p>
    </div>
  </div>
</footer>
<div class="bottom-bar">© www.harbornetcall.com.au — All rights reserved.</div>

</body>
</html>
```